Income Tax Flyer - Updates Needed

Just need to update this flyer design and give it a new look. We would like to keep all the same wording but make it stand out a little more. Our selling point is the "Same Day Tax Advance up to $6,000"

Industry/Entity Type

Lending, Small Loans, Tax Services, Title Loans, Personal Loans

```html
<!DOCTYPE html>
<html lang="en">
<head>
<meta charset="utf-8">
<title>Same Day Tax Advance Flyer</title>
<link rel="stylesheet" href="https://fonts.googleapis.com/css2?family=Cinzel:wght@700;900&family=Poppins:wght@500;600&display=swap">
<style>
  :root {
    --backdrop: #8a8a8a;
    --paper: #ffffff;
    --brand-red: #b3202a;
    --brand-green: #0f4d2c;
    --ink: #1c1c1c;
    --photo-dark: #3a2f2a;
    --photo-mid: #6b5a4e;
    --photo-light: #9a8f86;
  }
  html, body {
    margin: 0;
    padding: 0;
    width: 1200px;
    height: 2575px;
    overflow: hidden;
    background: var(--backdrop);
  }
  .flyer {
    position: absolute;
    left: 30px;
    top: 488px;
    width: 1140px;
    height: 1598px;
    box-shadow: 0 12px 30px rgba(0,0,0,0.35);
  }
  .flyer svg { display: block; width: 100%; height: 100%; }
  .brand-name { font-family: 'Poppins', sans-serif; font-weight: 600; font-size: 19px; fill: var(--brand-green); }
  .kicker { font-family: 'Cinzel', serif; font-weight: 700; font-size: 37px; fill: var(--brand-red); }
  .headline { font-family: 'Cinzel', serif; font-weight: 900; font-size: 76px; fill: var(--brand-green); }
  .apply-line { font-family: 'Poppins', sans-serif; font-weight: 600; font-size: 22px; fill: var(--brand-green); }
  .band-text { font-family: 'Poppins', sans-serif; font-weight: 600; font-size: 30px; fill: var(--paper); }
  .feature-text { font-family: 'Poppins', sans-serif; font-weight: 500; font-size: 18px; fill: var(--ink); }
  .contact-label { font-family: 'Poppins', sans-serif; font-weight: 500; font-size: 18px; fill: var(--paper); }
  .address { font-family: 'Poppins', sans-serif; font-weight: 500; font-size: 18px; fill: var(--ink); }
  .icon-line { fill: none; stroke: var(--paper); stroke-width: 1.6; stroke-linecap: round; stroke-linejoin: round; }
</style>
</head>
<body>
<div class="flyer">
  <svg viewBox="0 0 760 1065" xmlns="http://www.w3.org/2000/svg">
    <defs>
      <linearGradient id="photoTone" x1="0" y1="0" x2="1" y2="1">
        <stop offset="0" stop-color="var(--photo-light)"/>
        <stop offset="0.45" stop-color="var(--photo-mid)"/>
        <stop offset="1" stop-color="var(--photo-dark)"/>
      </linearGradient>
      <linearGradient id="bandShade" x1="0" y1="0" x2="0" y2="1">
        <stop offset="0" stop-color="#000" stop-opacity="0.18"/>
        <stop offset="1" stop-color="#000" stop-opacity="0"/>
      </linearGradient>
      <path id="bandCurve" d="M50 760 C260 790 480 785 712 738"/>
    </defs>

    <rect class="paper" width="760" height="1065" fill="var(--paper)"/>

    <!-- hero area -->
    <path class="hero-wave" d="M0 262 C130 340 300 428 490 430 C610 430 705 375 760 300 V330 C705 405 610 445 495 446 C300 446 130 360 0 278 Z" fill="var(--brand-red)"/>
    <path class="hero-photo" role="img" aria-label="Photo of two smiling business owners standing with arms crossed in front of their shop door"
          d="M0 0 H760 V300 C705 375 610 430 490 430 C300 428 130 340 0 262 Z" fill="url(#photoTone)"/>

    <!-- brand -->
    <circle class="brand-mark" cx="33" cy="447" r="9" fill="var(--brand-red)"/>
    <text class="brand-name" x="48" y="454">Ledgerline Financial</text>

    <!-- headline -->
    <text class="kicker" x="380" y="525" text-anchor="middle">Same Day Tax Advance</text>
    <text class="headline" x="381" y="592" text-anchor="middle">UP TO $6,000</text>
    <path class="headline-swoosh" d="M440 594 C500 622 570 620 610 582 C565 630 495 630 440 594 Z" fill="var(--brand-red)"/>

    <line x1="152" y1="640" x2="608" y2="640" stroke="var(--brand-red)" stroke-width="1.5"/>
    <text class="apply-line" x="380" y="670" text-anchor="middle">Apply Here For $5,000- $6,000 Today</text>
    <line x1="152" y1="682" x2="608" y2="682" stroke="var(--brand-red)" stroke-width="1.5"/>

    <!-- banner -->
    <path d="M0 790 C250 825 500 830 760 770 V840 C500 860 250 860 0 840 Z" fill="url(#bandShade)"/>
    <path class="banner" d="M0 712 C250 742 500 742 760 708 V770 C500 825 250 822 0 790 Z" fill="var(--brand-red)"/>
    <text class="band-text"><textPath href="#bandCurve">File Your Taxes and Apply For Easy Advance</textPath></text>

    <!-- features -->
    <g class="feature">
      <circle cx="95" cy="876" r="25" fill="var(--brand-red)"/>
      <circle class="icon-line" cx="95" cy="878" r="12"/>
      <line class="icon-line" x1="95" y1="862" x2="95" y2="866"/>
      <text x="95" y="882" text-anchor="middle" font-family="Poppins, sans-serif" font-size="10" font-weight="600" fill="var(--paper)">24</text>
      <text class="feature-text" x="152" y="871">Available In</text>
      <text class="feature-text" x="152" y="893">24Hours or Less</text>
    </g>
    <g class="feature">
      <circle cx="95" cy="946" r="25" fill="var(--brand-red)"/>
      <rect class="icon-line" x="83" y="937" width="24" height="13" rx="2"/>
      <circle class="icon-line" cx="95" cy="943.5" r="3"/>
      <path class="icon-line" d="M81 956 C88 952 96 958 108 954"/>
      <text class="feature-text" x="152" y="942">Choose Your</text>
      <text class="feature-text" x="152" y="964">Loan Amount</text>
    </g>
    <g class="feature">
      <circle cx="95" cy="1018" r="25" fill="var(--brand-red)"/>
      <path class="icon-line" d="M92 1030 V1012 a2.5 2.5 0 0 1 5 0 V1020 h5 a3 3 0 0 1 3 3 V1030"/>
      <path class="icon-line" d="M88 1004 l2 2 M95 1001 v3 M102 1004 l-2 2"/>
      <text class="feature-text" x="152" y="1013">Quick</text>
      <text class="feature-text" x="152" y="1035">and Easy</text>
    </g>

    <!-- contact -->
    <rect class="contact-tag" x="478" y="850" width="200" height="38" fill="var(--brand-red)"/>
    <text class="contact-label" x="578" y="875" text-anchor="middle">Contact Us Today!</text>
    <text class="address" x="578" y="922" text-anchor="middle">Address line 1</text>
    <text class="address" x="578" y="948" text-anchor="middle">Address line 2</text>
    <text class="address" x="578" y="972" text-anchor="middle">Address line 3</text>
  </svg>
</div>
</body>
</html>
```